Flyer für Restaurant
Zielgruppe
Deutsche Küche mit Südafrikanischen Flair
Restaurant was auch Feierlichkeiten anbieten
Jung und Alt
Aufgabenstellung
Farbe : Wein rot und grau
Erleben Sie bei uns einen Abend mit vielfältiger oder deutscher Küche und all ihren Rafinessen. Sehen Sie sich unser Restaurant Gasthaus Dornbeck an, das mit einer Vielzahl an schmackhaften Speisen begeistert und noch dazu urgemütlich ist. Absolute Erholung bietet an warmen Tagen unser toller Außenbereich.
Parken können Sie ganz einfach vor dem Restaurant auf unseren kostenlosen Parkplätzen. Uns ist es wichtig, dass wir alle Menschen willkommen heißen können. Aus diesem Grund haben wir einen barrierefreien Zugang. Gerne nehmen wir Ihre Reservierung entgegen. Freuen Sie sich auf einen wundervollen Aufenthalt mit idyllischem Flair in unserem Restaurant. Darüber hinaus können Sie uns einfach per Telefon unter +4957218640 kontaktieren.
Flyer um in Briefkasten zu werfen

```html
<!DOCTYPE html>
<html lang="de">
<head>
<meta charset="utf-8">
<title>Gasthaus Dornbeck – Flyer</title>
<link href="https://fonts.googleapis.com/css2?family=EB+Garamond:ital,wght@0,600;0,700;1,600&family=Fira+Sans:ital,wght@0,400;0,500;0,600;1,400;1,600;1,700&display=swap" rel="stylesheet">
<style>
  :root {
    --wine: #7a1c26;
    --wine-dark: #6b1620;
    --stage: #b8b6b8;
    --paper: #e7e7e7;
    --ink-grey: #5e5e5e;
    --title-grey: #646464;
    --white: #ffffff;
    --box-grey: #dcdcdc;
    --curve-grey: #b7b9b9;
  }
  * { margin: 0; padding: 0; box-sizing: border-box; }
  html, body { width: 1200px; height: 1130px; overflow: hidden; background: var(--stage); }
  .canvas { position: relative; width: 1200px; height: 1130px; }

  .flyer { position: absolute; overflow: hidden; }
  .flyer--front { left: 116px; top: 244px; width: 471px; height: 667px; background: var(--wine); }
  .flyer--back { left: 627px; top: 244px; width: 473px; height: 670px; background: var(--paper); }

  .shape-layer { position: absolute; left: 0; top: 0; }

  /* Front */
  .cutlery-mark { position: absolute; left: 335px; top: 300px; width: 95px; height: 250px; border-radius: 48px 48px 20px 20px; background: rgba(255,255,255,0.07); }
  .front-title { position: absolute; color: var(--white); font-family: "EB Garamond", serif; font-weight: 700; line-height: 1; white-space: nowrap; }
  .front-title__welcome { top: 279px; left: 32px; font-size: 53px; }
  .front-title__welcome em { font-style: italic; font-weight: 600; font-size: 38px; margin-left: 12px; }
  .front-title__name1 { top: 335px; left: 112px; font-size: 55px; }
  .front-title__name2 { top: 382px; left: 76px; font-size: 55px; }
  .cuisine { position: absolute; left: 72px; top: 452px; color: var(--white); font-family: "Fira Sans", sans-serif; font-weight: 500; font-size: 15px; letter-spacing: 0.16em; line-height: 27px; }
  .intro { position: absolute; left: 70px; top: 552px; color: var(--white); font-family: "Fira Sans", sans-serif; font-style: italic; font-size: 11px; letter-spacing: 0.05em; line-height: 16px; }
  .front-phone { position: absolute; left: 70px; top: 620px; display: flex; align-items: center; gap: 10px; color: var(--white); font-family: "Fira Sans", sans-serif; font-weight: 500; font-size: 15px; letter-spacing: 0.14em; }
  .house-photo { position: absolute; left: 287px; top: 485px; width: 151px; height: 152px; border-radius: 12px; border: 2px solid var(--white); background: linear-gradient(180deg, #3f6bb5 0%, #6f8fc8 18%, #e9dcc0 22%, #efe4cc 62%, #b9b9b1 80%, #8a8f80 100%); }

  /* Back */
  .back-title { position: absolute; left: 0; width: 100%; text-align: center; font-family: "EB Garamond", serif; font-weight: 700; line-height: 1; }
  .back-title__line1 { top: 180px; font-size: 36px; color: var(--wine); }
  .back-title__line1 span { color: var(--title-grey); }
  .back-title__line2 { top: 222px; font-size: 37px; color: var(--title-grey); }

  .occasions { position: absolute; left: 52px; top: 280px; list-style: none; font-family: "Fira Sans", sans-serif; font-size: 13.5px; color: var(--ink-grey); }
  .occasion { display: flex; align-items: center; gap: 16px; }
  .occasion + .occasion { margin-top: 14px; }
  .occasion__icon { width: 28px; height: 28px; flex: none; }
  .occasion__text { line-height: 20px; }

  .hours { position: absolute; left: 255px; top: 285px; width: 152px; height: 131px; border-radius: 18px; background: var(--box-grey); border: 2px solid #f3f3f3; padding: 16px 0 0 23px; font-family: "Fira Sans", sans-serif; font-size: 9.5px; color: var(--ink-grey); line-height: 13.5px; }
  .hours__times { font-weight: 600; margin: 8px 0 7px; line-height: 15.5px; }
  .hours strong { font-weight: 600; }

  .perks-heading { position: absolute; left: 55px; top: 424px; font-family: "Fira Sans", sans-serif; font-weight: 600; font-size: 13.5px; color: var(--wine); }
  .perks { position: absolute; left: 43px; top: 455px; list-style: none; font-family: "Fira Sans", sans-serif; font-size: 11.5px; color: var(--ink-grey); letter-spacing: 0.02em; }
  .perks li { line-height: 22px; }
  .perks li::before { content: "•"; display: inline-block; width: 12px; font-size: 9px; }

  .booking { position: absolute; left: 0; width: 100%; text-align: center; color: var(--white); font-family: "Fira Sans", sans-serif; font-style: italic; }
  .booking__lead { top: 562px; font-size: 15px; font-weight: 600; letter-spacing: 0.12em; }
  .booking__phone { top: 584px; font-size: 26px; font-weight: 700; }
  .booking__note { top: 627px; font-size: 11.5px; letter-spacing: 0.22em; }
</style>
</head>
<body>
<main class="canvas">

  <section class="flyer flyer--front">
    <svg class="shape-layer" width="471" height="667" viewBox="0 0 471 667">
      <defs>
        <linearGradient id="dishTones" x1="0" y1="0" x2="1" y2="1">
          <stop offset="0" stop-color="#e9c25c"/>
          <stop offset="0.5" stop-color="#c98a3c"/>
          <stop offset="1" stop-color="#f0c248"/>
        </linearGradient>
      </defs>
      <path d="M0,193 Q220,285 471,228 L471,245 Q220,300 0,205 Z" fill="#ece6df"/>
      <g role="img" aria-label="Foto: Schnitzel mit Pommes frites und Zitrone auf einem Teller">
        <path d="M0,0 L471,0 L471,228 Q220,285 0,193 Z" fill="url(#dishTones)"/>
      </g>
    </svg>
    <div class="cutlery-mark" role="img" aria-label="Dekoratives Besteck im Hintergrund"></div>

    <h1 class="front-title front-title__welcome">Willkommen<em>im</em></h1>
    <div class="front-title front-title__name1">Gasthaus</div>
    <div class="front-title front-title__name2">Dornbeck</div>

    <p class="cuisine">Deutsche Küche<br>mit südafrikanischen<br>Wurzeln.</p>
    <p class="intro">Unser Haus bietet für Jung<br>&amp; Alt ein entspanntes Ambiente<br>zum Wohlfühlen.</p>

    <div class="front-phone">
      <svg width="16" height="16" viewBox="0 0 24 24" aria-hidden="true"><path fill="#fff" d="M6.6 10.8a15.1 15.1 0 0 0 6.6 6.6l2.2-2.2c.3-.3.7-.4 1-.2 1.1.4 2.3.6 3.6.6.6 0 1 .4 1 1V20c0 .6-.4 1-1 1A17 17 0 0 1 3 4c0-.6.4-1 1-1h3.5c.6 0 1 .4 1 1 0 1.3.2 2.5.6 3.6.1.3 0 .7-.2 1z"/></svg>
      <span>05721-8640</span>
    </div>

    <div class="house-photo" role="img" aria-label="Foto: Außenansicht des Gasthauses mit Terrasse und Sonnenschirmen"></div>
  </section>

  <section class="flyer flyer--back">
    <svg class="shape-layer" width="473" height="670" viewBox="0 0 473 670">
      <defs>
        <linearGradient id="tableTones" x1="0" y1="0" x2="1" y2="0">
          <stop offset="0" stop-color="#5d5a63"/>
          <stop offset="0.35" stop-color="#8a7f86"/>
          <stop offset="0.7" stop-color="#b9b8bc"/>
          <stop offset="1" stop-color="#d8d8dc"/>
        </linearGradient>
      </defs>
      <g role="img" aria-label="Foto: festlich gedeckte Tafel mit Tulpen und Servietten">
        <rect x="0" y="0" width="473" height="240" fill="url(#tableTones)"/>
      </g>
      <path d="M0,175 Q200,40 473,180 L473,670 L0,670 Z" fill="var(--curve-grey)"/>
      <path d="M0,180 Q200,55 473,188 L473,670 L0,670 Z" fill="var(--wine)"/>
      <path d="M0,205 Q200,70 473,198 L473,670 L0,670 Z" fill="var(--white)"/>
      <path d="M0,222 Q200,78 473,210 L473,670 L0,670 Z" fill="var(--paper)"/>
      <rect x="360" y="440" width="60" height="115" rx="28" fill="#d4d4d4" opacity="0.45" role="img" aria-label="Dekoratives Besteck im Hintergrund"/>
      <path d="M0,578 Q240,484 473,584 L473,670 L0,670 Z" fill="var(--curve-grey)"/>
      <path d="M0,584 Q240,492 473,590 L473,670 L0,670 Z" fill="var(--white)"/>
      <path d="M0,588 Q240,498 473,594 L473,670 L0,670 Z" fill="var(--wine)"/>
    </svg>

    <h2 class="back-title back-title__line1">Ihre FEIER <span>im</span></h2>
    <div class="back-title back-title__line2">Gasthaus Dornbeck</div>

    <ul class="occasions">
      <li class="occasion">
        <svg class="occasion__icon" viewBox="0 0 28 28" aria-hidden="true" fill="none" stroke="#666" stroke-width="1.6"><rect x="4" y="14" width="20" height="10" rx="1"/><path d="M4 18 q3 2 5 0 t5 0 t5 0 t5 0"/><rect x="8" y="9" width="12" height="5"/><path d="M14 9 V5"/><path d="M14 2 q1.5 1.5 0 3 q-1.5 -1.5 0 -3" fill="#666"/></svg>
        <span class="occasion__text">Geburtstage</span>
      </li>
      <li class="occasion">
        <svg class="occasion__icon" viewBox="0 0 28 28" aria-hidden="true" fill="none" stroke="#666" stroke-width="1.6"><path d="M5 8 l6 2 l-1.5 7 q-3 1 -5 -1 z"/><path d="M7.5 17 l-2 8 M3 25 h5"/><path d="M23 8 l-6 2 l1.5 7 q3 1 5 -1 z"/><path d="M20.5 17 l2 8 M25 25 h-5"/><path d="M14 2 v3 M10 3 l1 2 M18 3 l-1 2"/></svg>
        <span class="occasion__text">Jubiläen</span>
      </li>
      <li class="occasion">
        <svg class="occasion__icon" viewBox="0 0 28 28" aria-hidden="true" fill="#666"><circle cx="6" cy="9" r="2.5"/><circle cx="14" cy="7" r="2.5"/><circle cx="22" cy="9" r="2.5"/><rect x="4" y="12" width="4" height="11" rx="1"/><rect x="12" y="10" width="4" height="13" rx="1"/><rect x="20" y="12" width="4" height="11" rx="1"/></svg>
        <span class="occasion__text">Vereinsabende &amp;<br>Firmenfeiern</span>
      </li>
    </ul>

    <div class="hours">
      <p>Wir haben an 5 Tagen<br>die Woche geöffnet:</p>
      <p class="hours__times">11.00 - 14.30 Uhr<br>17.00 - 20.00 Uhr</p>
      <p>Ruhetage sind<br><strong>Dienstag &amp; Mittwoch.</strong></p>
    </div>

    <h3 class="perks-heading">Besonders angenehm für Sie:</h3>
    <ul class="perks">
      <li>gemütliche Gasträume &amp; idyllischer Außenbereich</li>
      <li>barrierefreier Zugang</li>
      <li>kostenlose Parkplätze direkt vor dem Haus</li>
    </ul>

    <p class="booking booking__lead">Reservieren Sie gerne unter:</p>
    <p class="booking booking__phone">05721 - 8640</p>
    <p class="booking booking__note">Wir freuen uns darauf, Sie bei uns zu begrüßen!</p>
  </section>

</main>
</body>
</html>
```